Venbrisk Card

We want a business card that shows people who we are the log attached was designed by the designers on graft hive,we are using the OO in the logo (speech bubbles as our icon,so please make that part of the card ) keep the colouring the same as the logo design and we will be using high end production on the card using silver foil as the icon to make it stand out.
As Venbrisk we specialise in finding influencers through social networks for brands, so if you used yammo to comment about sports products and you were followed by of lot of users and interacted with those users then the algorithm finds you and we contact you to work for our clients as a company we then have a set of influencers that we use to support new sports products.
Also we use our algorithm to help athletes,models etc to be scored via there digital influence so when say Orvel QD ask me to find a skater that is not so much a podium rider but is more digital focused for a digital campaign then we work out who those guys or girls are to help Orvel QD
Venbrisk is the name of the product and company, However I just wanted to give you the rationale of why we chose venbrisk in the first place. Aldo itself is an 'abbreviation' from the proper name Aldemar Fusk from Keeper of the Vales. The character was able to look into the morvendal (sometimes translated as "Seeing Stone" but literally meaning "Farsighted" or "One that Sees from Afar") and see into the far corners of the Universe. Much in the same way as the platform has been developed is able to look into the far corners of the social network arena to help brands and Athletes will be able to see how they rated....but don't worry i don't go running around in the woods with a foam Axe and an army of dwarfs!!!
Digital Directors,Brand Directors,Athletes,Models,Celebrities and agents
Business

```html
<!DOCTYPE html>
<html lang="en">
<head>
<meta charset="utf-8">
<title>Venbrisk Business Card</title>
<link href="https://fonts.googleapis.com/css2?family=Open+Sans:wght@400;600&display=swap" rel="stylesheet">
<style>
  :root {
    --stage: #2b2b2d;
    --card-white: #f4f5f6;
    --card-black: #262626;
    --brand-blue: #3aa3dc;
    --ink: #3c3c3c;
    --ink-soft: #5a5a5a;
    --faint-grey: #e3e4e6;
    --silver: #d9d9d9;
  }
  * { box-sizing: border-box; margin: 0; padding: 0; }
  html, body {
    width: 1200px; height: 900px; overflow: hidden;
    background: var(--stage);
    font-family: "Open Sans", sans-serif;
  }
  .stage { position: relative; width: 1200px; height: 900px; }

  .card {
    position: absolute;
    width: 560px; height: 320px;
    border-radius: 3px;
    overflow: hidden;
    box-shadow: 0 10px 30px rgba(0,0,0,.35);
  }

  /* Front */
  .card-front { left: 80px; top: 90px; background: var(--card-white); color: var(--ink); }
  .front-mark {
    position: absolute; left: 300px; top: 120px;
    width: 210px; height: 210px; border-radius: 50%;
    background: var(--faint-grey);
  }
  .brand-name {
    position: absolute; left: 36px; top: 22px;
    font-size: 58px; font-weight: 600; letter-spacing: -1px;
    color: var(--brand-blue); line-height: 1;
  }
  .person { position: absolute; left: 40px; top: 100px; }
  .person-name { font-size: 22px; font-weight: 400; color: var(--ink); }
  .person-title { font-size: 11px; letter-spacing: .4px; color: var(--ink-soft); text-transform: uppercase; margin-top: 2px; }
  .contact-list { position: absolute; left: 40px; top: 168px; list-style: none; font-size: 14px; line-height: 1.55; }
  .contact-list .label { display: inline-block; width: 16px; color: var(--brand-blue); font-size: 12px; }
  .address {
    position: absolute; left: 318px; top: 228px;
    padding-left: 14px; border-left: 1.5px solid var(--brand-blue);
    font-size: 13px; line-height: 1.5; color: var(--ink);
  }
  .address .web { color: var(--brand-blue); font-weight: 600; }

  /* Back */
  .card-back {
    left: 560px; top: 490px; background: var(--card-black);
    display: flex; align-items: center; justify-content: center;
  }
  .back-name { font-size: 64px; font-weight: 600; letter-spacing: -1px; color: var(--silver); line-height: 1; }
</style>
</head>
<body>
<main class="stage">
  <section class="card card-front" aria-label="Card front">
    <div class="front-mark" aria-hidden="true"></div>
    <div class="brand-name">venbrisk</div>
    <div class="person">
      <p class="person-name">Corin Maddox</p>
      <p class="person-title">Marketing Director</p>
    </div>
    <ul class="contact-list">
      <li><span class="label">T</span>0400 555 218</li>
      <li><span class="label">M</span>03 9000 4417</li>
      <li><span class="label">E</span>cmaddox@venbrisk.com</li>
    </ul>
    <address class="address" style="font-style:normal">
      Level 3, 20 Harlow Lane<br>
      West Ashby VIC 3000<br>
      <span class="web">www.venbrisk.com</span>
    </address>
  </section>

  <section class="card card-back" aria-label="Card back">
    <span class="back-name">venbrisk</span>
  </section>
</main>
</body>
</html>
```